Dane Moro films- wedding and event films company website. DESKTOP AND MOBILE

We need a website for a high-end wedding and event film production company. Looking for a very modern and elegant design. my old website is www.danemorofilms.example

I like the "white/black/rose gold" color scheme of my logo.

really looking for a sleek modern design the breaths professional and artistic.

Target Market(s)

wedding and event films.

Industry/Entity Type

Film Production

Number of Pages Required

5+ page

Colors

Designer to choose colors to be used in the design.

Requirements
Must have
• website name will be www.danemorofilms.example
• tagline is "CINEMATIC STORIES ABOUT YOU"
• sections: HOME, CONTACT, ABOUT, FILMS, BLOG
• You can see my old website at danemorofilms.example
• Website about section:
• Dane Moro Films was Established with the basis of truly cinematic and artistic films in mind. Dane and his team routinely travel the globe documenting weddings and events for high profile clients and discerning couples. Dane was born and raised in Maui Hawaii and has a unique approach to his films that embody the essence of a Hollywood film. Dane has spent the last 10 years traveling the world documenting corporate events and weddings with multiple Award winning production companies. In 2017 Dane decided to establish his own brand “Dane Moro films” that will take everything he has learned with his past experiences and push it to the next level. Aside from his personal achievements, Dane is extremely passionate about his craft and always looks forward to handcrafting beautiful wedding/event films for his clients. The style of work is non-traditional and the day of filming is extremely unobtrusive (as we are looking for natural-candid/ raw emotions).
• If you are looking for the best price in town, we are probably not the best option, but if you’re looking for the best quality and peace of mind on your wedding day, then you’re in the right place. Dane Moro Films is a boutique studio that only accepts a limited number of assignments per year. Inquire early to ensure availability.
• LINKS TO VIMEO VIDEOS THAT WILL BE IN THE "FILMS' SECTION.
• BRENT FILM TRAILER - https://clipvault.example/418205736
• BRENT FEATURE FILM - https://clipvault.example/527910384
• NORA AND PAUL'S WEDDING - https://clipvault.example/649382015
• DRONE DEMO REEL - https://clipvault.example/751046923
• WEDDING INDUSTRY EVENT PARTY - https://clipvault.example/862937104/7a2d9c3e8b
• images that you can use on site are here: https://maribelortegaphotos.picvault.example/gallery/ruth&glen/
• password is: meadow

```html
<!DOCTYPE html>
<html lang="en">
<head>
<meta charset="utf-8">
<title>Dane Moro Films</title>
<link href="https://fonts.googleapis.com/css2?family=Poppins:wght@600;700&family=Roboto:wght@400&display=swap" rel="stylesheet">
<style>
  :root {
    --white: #ffffff;
    --ink: #1f1f1f;
    --nav-text: #333333;
    --rose-gold: #c89270;
    --rose-gold-light: #e4c2ad;
    --button-text: #3b2a22;
    --foliage-dark: #27331f;
    --foliage-mid: #4f5f3f;
    --foliage-pale: #8e958c;
    --stone: #c9c2c4;
    --terrace: #9c8c94;
    --sky: #b9b8c6;
    --shade: rgba(28, 26, 36, 0.30);
  }
  * { box-sizing: border-box; margin: 0; padding: 0; }
  html, body {
    width: 1200px;
    height: 611px;
    overflow: hidden;
    background: var(--white);
  }
  .site {
    position: relative;
    width: 1200px;
    height: 611px;
    font-family: "Roboto", Arial, sans-serif;
  }
  .site-header {
    position: absolute;
    top: 0; left: 0;
    width: 100%;
    height: 64px;
    background: var(--white);
    display: flex;
    align-items: center;
    padding: 0 20px;
  }
  .brand {
    display: flex;
    align-items: center;
    gap: 23px;
    color: var(--nav-text);
    font-size: 16px;
    text-decoration: none;
  }
  .brand-mark {
    width: 36px;
    height: 36px;
    border-radius: 50%;
    background: var(--rose-gold);
  }
  .main-nav {
    position: absolute;
    top: 0; left: 0;
    width: 100%;
    height: 64px;
    pointer-events: none;
  }
  .nav-link {
    position: absolute;
    top: 0;
    height: 64px;
    line-height: 64px;
    transform: translateX(-50%);
    font-size: 14px;
    letter-spacing: 0.2px;
    color: var(--nav-text);
    text-decoration: none;
    pointer-events: auto;
  }
  .nav-link.is-active { color: var(--ink); }
  .nav-link.is-active::after {
    content: "";
    position: absolute;
    left: 0; right: 0;
    bottom: 13px;
    height: 2px;
    background: var(--ink);
  }
  .hero {
    position: absolute;
    top: 64px; left: 0;
    width: 100%;
    height: 547px;
    overflow: hidden;
  }
  .hero-photo {
    position: absolute;
    inset: 0;
    background:
      radial-gradient(ellipse 260px 140px at 170px 420px, rgba(150,70,70,0.55), rgba(150,70,70,0) 70%),
      radial-gradient(ellipse 420px 220px at 110px 330px, rgba(170,176,168,0.55), rgba(170,176,168,0) 70%),
      radial-gradient(ellipse 520px 180px at 880px 480px, rgba(190,168,172,0.75), rgba(190,168,172,0) 75%),
      radial-gradient(ellipse 460px 90px at 960px 300px, rgba(214,206,204,0.7), rgba(214,206,204,0) 75%),
      radial-gradient(ellipse 300px 220px at 760px 250px, rgba(104,124,80,0.7), rgba(104,124,80,0) 70%),
      radial-gradient(ellipse 600px 200px at 600px 560px, rgba(200,204,190,0.45), rgba(200,204,190,0) 75%),
      linear-gradient(180deg, var(--sky) 0%, var(--stone) 45%, var(--terrace) 100%);
  }
  .hero-photo::before {
    content: "";
    position: absolute;
    inset: 0;
    background: linear-gradient(90deg, var(--foliage-dark) 0%, var(--foliage-mid) 35%, rgba(79,95,63,0.6) 52%, rgba(79,95,63,0) 64%);
  }
  .hero-shade {
    position: absolute;
    inset: 0;
    background: var(--shade);
  }
  .hero-content {
    position: absolute;
    inset: 0;
    text-align: center;
    color: var(--white);
    font-family: "Poppins", Arial, sans-serif;
  }
  .hero-title {
    position: absolute;
    top: 118px;
    left: 50%;
    transform: translateX(-50%);
    width: 560px;
    font-size: 84px;
    font-weight: 700;
    line-height: 107px;
  }
  .hero-tagline {
    position: absolute;
    top: 346px;
    left: 0; right: 0;
    font-size: 20px;
    font-weight: 700;
    letter-spacing: 0.2px;
  }
  .hero-button {
    position: absolute;
    top: 413px;
    left: 538px;
    width: 124px;
    height: 41px;
    line-height: 41px;
    border-radius: 3px;
    background: var(--rose-gold-light);
    color: var(--button-text);
    font-family: "Roboto", Arial, sans-serif;
    font-size: 16px;
    text-decoration: none;
    text-align: center;
  }
</style>
</head>
<body>
  <div class="site">
    <header class="site-header">
      <a class="brand" href="#home">
        <span class="brand-mark"></span>
        <span class="brand-name">Dane Moro Films</span>
      </a>
      <nav class="main-nav">
        <a class="nav-link is-active" href="#home" style="left:698px">HOME</a>
        <a class="nav-link" href="#contact" style="left:817px">CONTACT</a>
        <a class="nav-link" href="#about" style="left:939px">ABOUT</a>
        <a class="nav-link" href="#films" style="left:1050px">FILMS</a>
        <a class="nav-link" href="#blog" style="left:1156px">BLOG</a>
      </nav>
    </header>

    <section class="hero" id="home">
      <div class="hero-photo" role="img" aria-label="Wedding photograph: a bride and groom embracing on a garden terrace beside a stone balustrade, green hedges and red flowers"></div>
      <div class="hero-shade"></div>
      <div class="hero-content">
        <h1 class="hero-title">Dane Moro Films</h1>
        <p class="hero-tagline">CINEMATIC STORIES ABOUT YOU .</p>
        <a class="hero-button" href="#films">See More</a>
      </div>
    </section>
  </div>
</body>
</html>
```